Sign Front of Business

Sign for front of workshop. We want Tolvar Mechanical in same font and colour as logo then the logo after name. Would like a background colour maybe dark blue with a border.

Target Market(s)

Mining Community

Industry/Entity Type

Mechanical

Requirements
Must have
• Logo colours

```html
<!DOCTYPE html>
<html lang="en">
<head>
<meta charset="utf-8">
<title>Tolvar Mechanical – Workshop Sign</title>
<link rel="stylesheet" href="https://fonts.googleapis.com/css2?family=Orbitron:wght@900&display=swap">
<style>
  :root {
    --navy: #0b1a4a;
    --navy-deep: #07113a;
    --red: #b3080c;
    --red-dark: #5e0003;
    --black: #050505;
    --blue: #1f8ff0;
    --blue-dark: #0c4fb3;
    --silver-light: #ffffff;
    --silver-mid: #c9ccd1;
    --silver-dark: #7c8087;
  }
  html, body {
    margin: 0;
    padding: 0;
    width: 1200px;
    height: 300px;
    overflow: hidden;
    background: var(--navy);
  }
  .sign {
    position: relative;
    width: 1200px;
    height: 300px;
    background: var(--navy);
  }
  .sign__art {
    display: block;
    width: 1200px;
    height: 300px;
  }
  .sign__name,
  .sign__mark-name {
    font-family: "Orbitron", "Arial Black", sans-serif;
    font-weight: 900;
  }
</style>
</head>
<body>
<div class="sign">
  <svg class="sign__art" viewBox="0 0 1200 300" xmlns="http://www.w3.org/2000/svg">
    <defs>
      <linearGradient id="band-red" x1="0" y1="0" x2="1" y2="0">
        <stop offset="0" stop-color="var(--red)"/>
        <stop offset="0.6" stop-color="#8a0407"/>
        <stop offset="1" stop-color="var(--red)"/>
      </linearGradient>
      <linearGradient id="band-red-bottom" x1="0" y1="0" x2="1" y2="0">
        <stop offset="0" stop-color="var(--red)"/>
        <stop offset="0.7" stop-color="#8a0407"/>
        <stop offset="1" stop-color="var(--red-dark)"/>
      </linearGradient>
      <linearGradient id="streak-blue" x1="0" y1="0" x2="1" y2="0">
        <stop offset="0" stop-color="var(--blue)"/>
        <stop offset="1" stop-color="var(--blue)" stop-opacity="0"/>
      </linearGradient>
      <linearGradient id="tool-silver" x1="0" y1="0" x2="1" y2="0">
        <stop offset="0" stop-color="var(--silver-light)"/>
        <stop offset="0.5" stop-color="var(--silver-dark)"/>
        <stop offset="1" stop-color="var(--silver-light)"/>
      </linearGradient>
      <linearGradient id="name-blue" x1="0" y1="0" x2="0" y2="1">
        <stop offset="0" stop-color="#3aa6ff"/>
        <stop offset="0.55" stop-color="var(--blue)"/>
        <stop offset="1" stop-color="var(--blue-dark)"/>
      </linearGradient>
      <linearGradient id="name-silver" x1="0" y1="0" x2="0" y2="1">
        <stop offset="0" stop-color="var(--silver-light)"/>
        <stop offset="0.5" stop-color="var(--silver-mid)"/>
        <stop offset="0.52" stop-color="var(--silver-dark)"/>
        <stop offset="1" stop-color="var(--silver-light)"/>
      </linearGradient>
    </defs>

    <!-- background -->
    <rect class="sign__field" width="1200" height="300" fill="var(--navy)"/>

    <!-- top border -->
    <path class="sign__band sign__band--top" d="M0 0 H1200 V68 H1000 C920 68 860 25 760 25 H0 Z" fill="url(#band-red)"/>
    <rect class="sign__rule sign__rule--top" x="7" y="2" width="1186" height="6" fill="var(--black)"/>
    <rect class="sign__streak" x="0" y="60" width="340" height="5" fill="url(#streak-blue)"/>

    <!-- bottom border -->
    <path class="sign__band sign__band--bottom" d="M0 236 H240 C360 236 380 283 520 283 H1200 V300 H0 Z" fill="url(#band-red-bottom)"/>
    <rect class="sign__rule sign__rule--bottom" x="134" y="283" width="1059" height="10" fill="var(--black)"/>

    <!-- tools -->
    <rect class="sign__tool sign__tool--top" x="370" y="44" width="620" height="18" rx="9"
          fill="url(#tool-silver)" role="img" aria-label="Spanner illustration"/>
    <rect class="sign__tool sign__tool--bottom" x="198" y="231" width="632" height="18" rx="9"
          fill="url(#tool-silver)" role="img" aria-label="Spanner illustration"/>

    <!-- business name -->
    <text class="sign__name" y="184" font-size="82">
      <tspan class="sign__name-lead" x="20" fill="url(#name-blue)" textLength="330" lengthAdjust="spacingAndGlyphs">TOLVAR</tspan>
      <tspan class="sign__name-trade" x="366" fill="url(#name-silver)" textLength="624" lengthAdjust="spacingAndGlyphs">MECHANICAL</tspan>
    </text>

    <!-- mark -->
    <g class="sign__mark">
      <circle class="sign__mark-disc" cx="1100" cy="150" r="92" fill="var(--blue)"/>
      <text class="sign__mark-name" x="1100" y="166" font-size="44" text-anchor="middle" fill="var(--navy-deep)">KRT</text>
    </g>
  </svg>
</div>
</body>
</html>
```